Kestrel Works Business Cards

This job is for the design of a business card.
I would like to review the design in 2x colour tones to choose from black and white inverted.
EG:
Black with white logo and white with black logo on BACK
White with black text on front and black with white text options
PRINTING DIMENSIONS: 4.5 x 8.5cm
Complete design will need to be provided in ready to print format with bleed lines
Target Market(s)
The audience of my business are people in the trade industry.
It will be also used for general networking with trades people and possible future clients.
I want to be represented as a professional, dynamic, creative and personable operator.
The card should reflect style, taste, experience, professionalism.
Industry/Entity Type
Business
Requirements
Must have
- BACK CONTENT:
- Logo in white and black background and vice versa with WHITE card and black logo review samples.
- FRONT CARD CONTENT:
- Name: Morgan Telvane
- Director
- Phone: 0438 216 947
- Email: morgan@kestrelworks.com.au
- Web: kestrelworks.com.au
- LICENCE #: KT-R 72158
Nice to have
- Possibly a textured background design on rear as a pose to a solid black
- Possibly adding a blue or orange discreet colour tone (possibly for email, phone abbreviated letter or symbols).

```html
<!DOCTYPE html>
<html lang="en">
<head>
<meta charset="utf-8">
<title>Kestrel Works Business Cards</title>
<link rel="stylesheet" href="https://fonts.googleapis.com/css2?family=PT+Sans:wght@400;700&display=swap">
<style>
  :root {
    --ink: #000000;
    --paper: #ffffff;
    --accent-blue: #2b2f8f;
    --accent-red: #e3262b;
    --panel-dark: #1c1c1c;
    --panel-mid: #3a3a3a;
    --edge-grey: #d4d4d4;
  }
  html, body {
    margin: 0;
    padding: 0;
    width: 1045px;
    height: 1200px;
    overflow: hidden;
    background: var(--paper);
    font-family: "PT Sans", "Myriad Pro", Arial, sans-serif;
  }
  .sheet { position: relative; width: 1045px; height: 1200px; }

  .card {
    position: absolute;
    width: 497px;
    height: 265px;
    box-sizing: border-box;
    overflow: hidden;
  }
  .card--dark { background: var(--ink); color: var(--paper); }
  .card--light { background: var(--paper); color: var(--ink); border: 2px solid var(--ink); }
  .card--framed-blue {
    border-left: 3px solid var(--accent-blue);
    border-right: 3px solid var(--accent-blue);
    border-bottom: 3px solid var(--accent-blue);
  }
  .card--modern { background: var(--paper); color: var(--ink); border: 1px solid var(--edge-grey); }

  .pos-front-a { left: 0; top: 0; }
  .pos-front-b { left: 548px; top: 0; }
  .pos-back-a  { left: 0; top: 279px; }
  .pos-back-b  { left: 548px; top: 279px; }
  .pos-front-c { left: 0; top: 646px; }
  .pos-front-d { left: 548px; top: 646px; }
  .pos-back-c  { left: 0; top: 935px; }
  .pos-back-d  { left: 548px; top: 935px; }

  /* front: classic layout */
  .holder {
    position: absolute;
    right: 24px;
    top: 8px;
    text-align: right;
  }
  .holder__name { font-size: 34px; line-height: 1.15; font-weight: 400; }
  .holder__role { font-size: 20px; line-height: 1.3; }
  .contact {
    position: absolute;
    left: 10px;
    bottom: 10px;
    margin: 0;
    padding: 0;
    list-style: none;
    font-size: 20px;
    line-height: 35px;
  }

  /* back: wordmark */
  .wordmark {
    position: absolute;
    left: 0; right: 0; top: 0; bottom: 0;
    display: flex;
    align-items: center;
    justify-content: center;
    gap: 16px;
  }
  .wordmark__square { width: 30px; height: 30px; background: currentColor; }
  .wordmark__square--blue { background: var(--accent-blue); }
  .wordmark__square--red { background: var(--accent-red); }
  .wordmark__name {
    font-size: 52px;
    font-weight: 700;
    letter-spacing: 1px;
    text-transform: uppercase;
    line-height: 1;
  }

  /* front: modern layout */
  .modern__art { position: absolute; left: 0; top: 0; }
  .modern__name {
    position: absolute;
    left: 28px;
    top: 16px;
    font-size: 34px;
    color: var(--accent-red);
    line-height: 1.1;
  }
  .modern__badge {
    position: absolute;
    right: 18px;
    top: 22px;
    display: flex;
    align-items: center;
    gap: 6px;
    color: var(--paper);
    font-size: 17px;
    font-weight: 700;
    text-transform: uppercase;
  }
  .modern__badge-square { width: 10px; height: 10px; background: var(--accent-red); }
  .modern__details {
    position: absolute;
    left: 0;
    width: 340px;
    top: 86px;
    text-align: center;
    font-size: 18px;
    line-height: 32px;
  }
  .modern__role { font-size: 22px; }
</style>
</head>
<body>
<main class="sheet">

  <!-- Set 1: black front -->
  <section class="card card--dark pos-front-a">
    <div class="holder">
      <div class="holder__name">Morgan Telvane</div>
      <div class="holder__role">Director</div>
    </div>
    <ul class="contact">
      <li>tel: 0438 216 947</li>
      <li>morgan@kestrelworks.com.au</li>
      <li>www.kestrelworks.com.au</li>
      <li>Licence #: KT-R 72158</li>
    </ul>
  </section>

  <!-- Set 2: white front -->
  <section class="card card--light pos-front-b">
    <div class="holder">
      <div class="holder__name">Morgan Telvane</div>
      <div class="holder__role">Director</div>
    </div>
    <ul class="contact">
      <li>tel: 0438 216 947</li>
      <li>morgan@kestrelworks.com.au</li>
      <li>www.kestrelworks.com.au</li>
      <li>Licence #: KT-R 72158</li>
    </ul>
  </section>

  <!-- Set 1: black back -->
  <section class="card card--dark pos-back-a">
    <div class="wordmark">
      <span class="wordmark__square"></span>
      <span class="wordmark__name">Kestrel Works</span>
    </div>
  </section>

  <!-- Set 2: white back -->
  <section class="card card--light pos-back-b">
    <div class="wordmark">
      <span class="wordmark__square"></span>
      <span class="wordmark__name">Kestrel Works</span>
    </div>
  </section>

  <!-- Set 3: black front with blue frame -->
  <section class="card card--dark card--framed-blue pos-front-c">
    <div class="holder">
      <div class="holder__name">Morgan Telvane</div>
      <div class="holder__role">Director</div>
    </div>
    <ul class="contact">
      <li>tel: 0438 216 947</li>
      <li>morgan@kestrelworks.com.au</li>
      <li>www.kestrelworks.com.au</li>
      <li>Licence #: KT-R 72158</li>
    </ul>
  </section>

  <!-- Set 4: white front with dark panel -->
  <section class="card card--modern pos-front-d">
    <svg class="modern__art" width="497" height="265" viewBox="0 0 497 265" aria-hidden="true">
      <defs>
        <linearGradient id="panel-fill" x1="0" y1="0" x2="1" y2="1">
          <stop offset="0" stop-color="var(--panel-mid)"/>
          <stop offset="1" stop-color="var(--panel-dark)"/>
        </linearGradient>
      </defs>
      <polygon points="300,0 497,0 497,265 362,265" fill="url(#panel-fill)"/>
      <line x1="0" y1="64" x2="310" y2="64" stroke="var(--accent-red)" stroke-width="3"/>
      <line x1="0" y1="73" x2="312" y2="73" stroke="var(--accent-red)" stroke-width="3"/>
      <line x1="300" y1="0" x2="362" y2="265" stroke="var(--accent-red)" stroke-width="3"/>
    </svg>
    <div class="modern__name">Morgan Telvane</div>
    <div class="modern__badge">
      <span class="modern__badge-square"></span>
      <span>Kestrel Works</span>
    </div>
    <div class="modern__details">
      <div class="modern__role">Director</div>
      <div>tel: 0438 216 947</div>
      <div>morgan@kestrelworks.com.au</div>
      <div>www.kestrelworks.com.au</div>
      <div>Licence #: KT-R 72158</div>
    </div>
  </section>

  <!-- Set 3: black back, blue accent -->
  <section class="card card--dark pos-back-c">
    <div class="wordmark">
      <span class="wordmark__square wordmark__square--blue"></span>
      <span class="wordmark__name">Kestrel Works</span>
    </div>
  </section>

  <!-- Set 4: black back, red accent -->
  <section class="card card--dark pos-back-d">
    <div class="wordmark">
      <span class="wordmark__square wordmark__square--red"></span>
      <span class="wordmark__name">Kestrel Works</span>
    </div>
  </section>

</main>
</body>
</html>
```